Vellora Labs - Mushroom Supplement Packaging

Our brand is called Vellora Labs. I've added a couple different logos that you can use. We are creating a line up of Mushroom Supplement products. I will add the entire line-up of products here. I've added examples of other products and packaging shape types I can purchase. Give me different options for packaging that is minimalist and clean for this brand that makes it look really well made and clean and make people want to buy.

Product 1 Lions Mane 1g
Product 2 Cordyceps 1g
Product 3 Chaga 1g
Product 4 Turkey Tail 1g
Product 5 Reishi 1g
Product 6 Maitake 1g
Product 7 Shiitake 1g

Product 8 (Mix) Lions Mane 143mg
Cordyceps 143mg
Chaga 143mg
Turkey Tail 143mg
Reishi 143mg
Maitake 143mg
Shiitake 143mg

```html
<!DOCTYPE html>
<html lang="en">
<head>
<meta charset="UTF-8">
<title>Vellora Labs – Lion's Mane Label</title>
<link href="https://fonts.googleapis.com/css2?family=Montserrat:wght@300;400;500;600;700;800&display=swap" rel="stylesheet">
<style>
  :root {
    --page: #ffffff;
    --label-dark: #121212;
    --label-mid: #3a3a3a;
    --label-light: #6e6e6e;
    --ink-white: #f2f2f2;
    --ink-soft: #d6d6d6;
    --ink-shadow: #2b2b2b;
    --copper: #b06a3a;
    --copper-deep: #7a3a17;
    --copper-light: #ecc7a6;
  }
  * { margin: 0; padding: 0; box-sizing: border-box; }
  html, body {
    width: 1200px; height: 857px; overflow: hidden;
    background: var(--page);
    font-family: "Montserrat", sans-serif;
  }
  .canvas { position: relative; width: 1200px; height: 857px; }
  .label {
    position: absolute; left: 407px; top: 289px; width: 372px; height: 357px;
    background: linear-gradient(90deg, var(--label-dark) 0%, var(--label-mid) 45%, var(--label-light) 100%);
    color: var(--ink-white);
  }
  .label > * { position: absolute; left: 0; right: 0; text-align: center; }
  .brand {
    top: 42px; font-size: 19px; font-weight: 600; letter-spacing: 2px;
    color: var(--ink-soft); line-height: 1.2;
  }
  .product-name {
    top: 117px; font-size: 38px; font-weight: 800; letter-spacing: 0.5px;
    line-height: 1; color: var(--ink-white);
  }
  .product-type {
    top: 157px; font-size: 24px; font-weight: 300; letter-spacing: 1px;
    color: var(--ink-shadow); line-height: 1;
  }
  .support-lead {
    top: 201px; font-size: 9.5px; font-weight: 400; letter-spacing: 1px;
    color: var(--ink-soft); line-height: 1;
  }
  .benefits {
    top: 214px; left: 59px; right: auto; width: 252px; height: 21px;
    border-radius: 11px;
    background: linear-gradient(90deg, var(--copper-light) 0%, var(--copper) 18%, var(--copper-deep) 50%, var(--copper) 80%, var(--copper-light) 100%);
    font-size: 12.5px; font-weight: 700; line-height: 21px; color: var(--copper-light);
    letter-spacing: 0;
    white-space: nowrap;
  }
  .dose { top: 255px; line-height: 1; }
  .dose-value { font-size: 46px; font-weight: 700; color: var(--ink-white); }
  .dose-unit { font-size: 24px; font-weight: 300; vertical-align: 19px; color: var(--ink-soft); }
  .badge {
    top: 313px; left: 13px; right: auto; width: 30px; height: 30px;
    border: 1px solid var(--copper);
  }
  .footer {
    top: 324px; display: flex; justify-content: center; align-items: center; gap: 5px;
  }
  .count { font-size: 12.5px; font-weight: 600; letter-spacing: 0.3px; color: var(--ink-soft); }
  .divider { width: 1px; height: 24px; background: var(--ink-soft); }
  .category { font-size: 10px; font-weight: 400; letter-spacing: 0.5px; text-align: left; line-height: 1.2; color: var(--ink-soft); }
</style>
</head>
<body>
  <main class="canvas">
    <section class="label">
      <div class="brand">VELLORA LABS</div>
      <h1 class="product-name">LION'S MANE</h1>
      <div class="product-type">MUSHROOM</div>
      <div class="support-lead">HELPS SUPPORT</div>
      <div class="benefits">MEMORY - FOCUS - NERVE HEALTH</div>
      <div class="dose"><span class="dose-value">1</span><span class="dose-unit">G</span></div>
      <div class="badge" aria-hidden="true"></div>
      <div class="footer">
        <span class="count">60 CAPSULES</span>
        <span class="divider"></span>
        <span class="category">DIETARY<br>SUPPLEMENT</span>
      </div>
    </section>
  </main>
</body>
</html>
```